Webdesign für  Photovoltaikanlagen und E-Ladeinfrastruktur
Webdesign für Photovoltaikanlagen und E-Ladeinfrastruktur
Zielgruppe
Die VALMO Energy GmbH ist ein Spezialist für die Planung und Projektierung von Photovoltaikanlagen und E-Ladeinfrastruktur.
Aufgabenstellung
- Design-Tool: Adobe Photoshop
- Hinweis: Die Firma wird sich neue aufstellen, was das Leistungsangebot betrifft. Sie können sich deshalb nur bedingt an der derzeitigen Website orientieren, alle fremden Logos (wie z.b. ORUPA) dürfen nicht mehr genutzt werden
- Gern hätten wir einen 'frischen' Slogan im headerbild

```html
<!DOCTYPE html>
<html lang="de">
<head>
<meta charset="utf-8">
<title>VALMO Energy GmbH</title>
<link href="https://fonts.googleapis.com/css2?family=Dosis:wght@400;500;600;700;800&display=swap" rel="stylesheet">
<style>
:root{
  --green:#1b6e5b;
  --green-dark:#155a4a;
  --text:#222;
  --bg:#f8f8f8;
  --btn:#e2e2e2;
  --footer:#f1f1f1;
  --white:#fff;
}
*{margin:0;padding:0;box-sizing:border-box}
html,body{width:1200px;height:2386px;overflow:hidden}
body{background:var(--bg);font-family:'Dosis',sans-serif;color:var(--text);position:relative}
.abs{position:absolute}

.site-header{left:0;top:0;width:1200px;height:110px;background:var(--bg)}
.brand{left:50px;top:28px;display:flex;align-items:center;gap:10px;font-weight:800;font-size:38px;color:var(--green);letter-spacing:1px}
.brand-mark{width:26px;height:26px;background:var(--green)}
.main-nav{left:271px;top:50px;display:flex;gap:30px;font-size:14px;font-weight:500;text-transform:uppercase}
.main-nav a{color:var(--text);text-decoration:none}
.main-nav a.active{color:var(--green)}

.hero{left:0;top:110px;width:1200px;height:608px;background:linear-gradient(180deg,#8fb1d6 0%,#cbdbe9 45%,#bfc8b0 62%,#7f8a6f 75%,#b9b7b3 100%)}
.hero-title{left:613px;top:195px;font-size:62px;font-weight:700;color:var(--green);letter-spacing:-1px}
.hero-lead{left:617px;top:278px;width:480px;font-size:27px;line-height:38px;font-weight:500;color:#222}
.hero-lead a{color:var(--green);font-weight:700;text-decoration:underline;text-underline-offset:4px}

.about-photo{left:100px;top:836px;width:454px;height:285px;background:linear-gradient(180deg,#5f8fc4 0%,#9cbbd8 40%,#e7d44a 55%,#d7c440 100%)}
.section-title{font-size:36px;font-weight:700;color:var(--green)}
.about-title{left:623px;top:862px}
.body-text{font-size:14.5px;line-height:21px;font-weight:500}
.about-text{left:623px;top:915px;width:420px}
.btn{display:flex;align-items:center;justify-content:center;width:127px;height:42px;border-radius:12px;background:var(--btn);font-size:15px;font-weight:700;color:#333;text-transform:uppercase;letter-spacing:.5px;box-shadow:0 1px 2px rgba(0,0,0,.15)}
.about-btn{left:625px;top:1014px}

.team-band{left:0;top:1256px;width:1200px;height:398px;background:linear-gradient(110deg,#1e3c78 0%,#3b5fa0 40%,#6f86ae 70%,#a9bad3 100%)}
.team-title{left:92px;top:1350px;font-size:35px;font-weight:700;color:var(--white)}
.team-text{left:92px;top:1400px;width:420px;color:var(--white)}
.team-btn{left:93px;top:1501px}

.projects-title{left:92px;top:1740px}
.projects-title small{font-size:14px;font-weight:500;color:var(--text);margin-left:6px}
.project-card{top:1807px;width:242px;height:308px;background:#f6f6f6;box-shadow:0 1px 4px rgba(0,0,0,.25)}
.project-photo{width:242px;height:180px}
.project-body{padding:12px 13px}
.project-body h3{font-size:14px;font-weight:700;line-height:20px}
.project-body p{font-size:13.5px;line-height:20px;font-weight:500}
.btn-small{display:inline-flex;margin-top:12px;width:72px;height:26px;border-radius:8px;background:var(--btn);font-size:9px;font-weight:700;align-items:center;justify-content:center;color:#333}
.slider-arrow{top:1932px;width:33px;height:33px}

.site-footer{left:0;top:2241px;width:1200px;height:145px;background:var(--footer);border-top:3px solid var(--green)}
.footer-nav{left:92px;top:2264px;display:flex;gap:28px;font-size:13.5px;font-weight:500;text-transform:uppercase}
.footer-address{left:811px;top:2264px;font-size:13.5px;line-height:19px;font-weight:500}
.footer-address strong{color:var(--green);font-weight:700}
.footer-contact{left:978px;top:2264px;font-size:13.5px;line-height:19px;font-weight:500}
</style>
</head>
<body>

<header class="site-header abs">
  <div class="brand abs"><span class="brand-mark"></span>VALMO</div>
  <nav class="main-nav abs">
    <a class="active" href="#">Home</a><a href="#">Unternehmen</a><a href="#">Projekte</a><a href="#">E-Ladeinfrastruktur</a><a href="#">Photovoltaik</a><a href="#">Planung &amp; Projektierung</a><a href="#">Jobs</a><a href="#">Kontakt</a>
  </nav>
</header>

<section class="hero abs" role="img" aria-label="Ladesäulen für Elektroautos auf einer Terrasse vor Hecke und Meer"></section>
<h1 class="hero-title abs">Gut vernetzt.</h1>
<p class="hero-lead abs">Ihr Spezialist für die <a href="#">Planung und Projektierung</a> von <a href="#">Photovoltaikanlagen</a> und <a href="#">E-Ladeinfrastruktur</a>.</p>

<div class="about-photo abs" role="img" aria-label="Firmengebäude mit gelber Fassade unter blauem Himmel"></div>
<h2 class="section-title about-title abs">Unternehmen</h2>
<p class="body-text about-text abs">Lorem ipsum dolor sit amet, consectetuer adipiscing elit. Aenean commodo ligula eget dolor. Aenean massa. Cum sociis natoque penatibus et magnis dis parturient montes, nascetur ridiculus mus. Donec quam felis, ultricies nec, pellentesque eu,</p>
<a class="btn about-btn abs">Mehr Infos</a>

<section class="team-band abs" role="img" aria-label="Monteur legt die Hand auf ein Solarmodul"></section>
<h2 class="team-title abs">Komm ins Team!</h2>
<p class="body-text team-text abs">Lorem ipsum dolor sit amet, consectetuer adipiscing elit. Aenean commodo ligula eget dolor. Aenean massa. Cum sociis natoque penatibus et magnis dis parturient montes, nascetur ridiculus mus. Donec quam felis, ultricies nec, pellentesque eu,</p>
<a class="btn team-btn abs">Mehr Infos</a>

<h2 class="section-title projects-title abs">Projekte<small>(Auszug)</small></h2>

<svg class="slider-arrow abs" style="left:42px" viewBox="0 0 33 33"><circle cx="16.5" cy="16.5" r="16.5" fill="var(--green)"/><path d="M19 9l-7 7.5 7 7.5" stroke="#fff" stroke-width="3.5" fill="none" stroke-linecap="round" stroke-linejoin="round"/></svg>
<svg class="slider-arrow abs" style="left:1126px" viewBox="0 0 33 33"><circle cx="16.5" cy="16.5" r="16.5" fill="var(--green)"/><path d="M14 9l7 7.5-7 7.5" stroke="#fff" stroke-width="3.5" fill="none" stroke-linecap="round" stroke-linejoin="round"/></svg>

<article class="project-card abs" style="left:92px">
  <div class="project-photo" role="img" aria-label="Einfamilienhaus mit Solarmodulen auf dem Dach" style="background:linear-gradient(180deg,#9cb8cf,#5f6f88 50%,#d8dadb)"></div>
  <div class="project-body"><h3>Lorem ipsum dolor sit amet</h3><p>Consectetuer adipiscing elit nean commodo ligula eget dolor.</p><span class="btn-small">DETAILS</span></div>
</article>
<article class="project-card abs" style="left:350px">
  <div class="project-photo" role="img" aria-label="Freistehende Solaranlage zwischen Bäumen" style="background:linear-gradient(180deg,#7fa6cf,#8aa070 55%,#4f6a35)"></div>
  <div class="project-body"><h3>Lorem ipsum dolor sit amet</h3><p>Consectetuer adipiscing elit nean commodo ligula eget dolor.</p><span class="btn-small">DETAILS</span></div>
</article>
<article class="project-card abs" style="left:609px">
  <div class="project-photo" role="img" aria-label="Luftbild einer Halle mit großer Dach-Solaranlage" style="background:linear-gradient(160deg,#8a7a55,#3f5f9a 45%,#2c4a86 70%,#c5503a)"></div>
  <div class="project-body"><h3>Lorem ipsum dolor sit amet</h3><p>Consectetuer adipiscing elit nean commodo ligula eget dolor.</p><span class="btn-small">DETAILS</span></div>
</article>
<article class="project-card abs" style="left:868px">
  <div class="project-photo" role="img" aria-label="Ladesäulen auf einem Parkplatz unter Bäumen" style="background:linear-gradient(180deg,#4e6a3a,#7d8a6a 50%,#c9c3b6)"></div>
  <div class="project-body"><h3>Lorem ipsum dolor sit amet</h3><p>Consectetuer adipiscing elit nean commodo ligula eget dolor.</p><span class="btn-small">DETAILS</span></div>
</article>

<footer class="site-footer abs"></footer>
<nav class="footer-nav abs"><span>Unternehmen</span><span>E-Ladeinfrastruktur</span><span>Photovoltaik</span><span>Planung &amp; Projektierung</span></nav>
<address class="footer-address abs" style="font-style:normal"><strong>VALMO Energy GmbH</strong><br>Lindenhofweg 14<br>09120 Talstadt</address>
<div class="footer-contact abs">Tel.: 01 23 456 78-20<br>Fax: 01 23 456 78-211<br>info@valmo-energy.de</div>

</body>
</html>
```